New website for a personal transformation academy

We need a website with a landing page and five sub-pages and either pages under each or one page where it is possible to jump between sections. The site will need to have a choice between two languages (English & Icelandic).
Needed functionality is:
Landing page with a link to social media posts, mail list registration, Meetwall messenger option and testimonies
1. Brindmoor Academy information with an option to add videos and registration sheet, see details attached
2. Vireltones, see details attached
3. Personal vireltones, information and order sheet
4. From Metatron, informational text
5. About us, CV with the option of adding video
Further details in the attached picture.
Brindmoor Academy is a new organisation that provides group training for a year where people go through a series of workshops to heal and release emotions, get to know the real you better and support you in realizing your dreams. The end goal is personal transformation. We work with meditations, archangels, masters and elementals.
Logo and colours are attached. The fonts used are CinzelDecorative and TrajanPro.

```html
<!DOCTYPE html>
<html lang="en">
<head>
<meta charset="utf-8">
<title>Brindmoor Academy</title>
<link rel="stylesheet" href="https://fonts.googleapis.com/css2?family=Cinzel+Decorative:wght@400;700;900&family=Cinzel:wght@400;700&family=Heebo:wght@400;500;700&display=swap">
<style>
:root{
  --navy:#14115a;
  --navy-deep:#100d4c;
  --panel:#1d1968;
  --purple:#6f14a6;
  --violet:#8a2fc4;
  --white:#ffffff;
  --muted:#d8d6f0;
}
*{box-sizing:border-box;margin:0;padding:0}
html,body{width:1200px;height:3327px;overflow:hidden;background:var(--navy)}
body{position:relative;font-family:"Heebo",sans-serif;color:var(--white)}
.abs{position:absolute}

/* header */
.site-header{left:0;top:0;width:1200px;height:75px;background:var(--navy)}
.brand-badge{left:124px;top:2px;width:124px;height:124px;border-radius:50%;background:var(--navy);display:flex;align-items:flex-end;justify-content:center;padding-bottom:26px;z-index:3;font-family:"Cinzel",serif;font-weight:700;font-size:15px;letter-spacing:.5px}
.main-nav{top:26px;left:510px;font-weight:700;font-size:15px;letter-spacing:.3px}
.main-nav a{position:absolute;white-space:nowrap;color:var(--white);text-decoration:none}
.nav-search{left:1006px;top:28px}
.lang{left:1050px;top:26px;font-weight:700;font-size:15px}

/* hero */
.hero{left:0;top:75px;width:1200px;height:599px;background:linear-gradient(120deg,#b9a8dc 0%,#8d72c9 30%,#a98fd6 55%,#7a60c0 80%,#3c2a8a 100%)}
.hero-figure{left:110px;top:15px;width:450px;height:584px;border-radius:200px 200px 40px 40px;background:radial-gradient(ellipse at 50% 55%,#c77ab8 0%,#4a36a8 45%,#2a2090 80%);opacity:.85}
.hero-title{left:597px;top:236px;font-family:"Cinzel Decorative",serif;font-weight:700;font-size:64px;line-height:80px;color:var(--navy);letter-spacing:2px;white-space:nowrap}
.hero-text{left:597px;top:344px;width:470px;font-size:16px;line-height:30px;color:var(--white)}
.btn{display:flex;align-items:center;justify-content:center;font-family:"Cinzel",serif;font-weight:700;color:var(--white)}
.hero-btn{left:597px;top:452px;width:168px;height:49px;background:var(--navy);font-size:16px}

/* section headings */
.section-title{left:0;width:1200px;text-align:center;font-family:"Cinzel Decorative",serif;font-size:40px;font-weight:400}
.section-title b{font-weight:900}
.rule{width:38px;height:4px;background:var(--purple);left:581px}

/* feed */
.filters{top:840px;left:0;width:1200px;font-size:16px}
.filters span{position:absolute;display:flex;align-items:center;gap:9px;white-space:nowrap}
.filters i{display:inline-block;width:14px;height:14px;border-radius:2px;background:var(--white)}
.filter-active{color:var(--violet)}
.filter-active::after{content:"";position:absolute;left:-10px;right:-10px;top:30px;height:2px;background:var(--violet)}

.post{background:var(--panel);width:311px;overflow:hidden}
.post h3{font-family:"Cinzel",serif;font-weight:400;font-size:21px;line-height:28px;margin:12px 14px 0;letter-spacing:.5px;display:flex;justify-content:space-between;align-items:center;white-space:nowrap}
.post h3 i{width:18px;height:18px;border:2px solid var(--white);border-radius:4px;margin-right:2px}
.post .likes{font-weight:700;font-size:14px;line-height:20px;margin:11px 14px 0}
.post p{font-size:13px;line-height:30px;margin:6px 14px 0}
.post .media{position:absolute;left:0;bottom:0;width:311px}
.m-sunset{height:133px;background:linear-gradient(180deg,#5a4a3a,#e89a2c 55%,#3a2612)}
.m-crowd{height:183px;background:linear-gradient(180deg,#dfe3ea,#8e939c 45%,#1c1c22)}
.m-night{height:183px;background:linear-gradient(180deg,#15182a,#33354a 55%,#9a6a3a 68%,#0a0a10)}
.m-light{height:183px;background:radial-gradient(circle at 50% 40%,#ffffff,#cfe0f6 40%,#9fb7e6 70%,#e2b9d8)}
.m-aura{height:183px;background:radial-gradient(circle at 50% 50%,#ffffff 0,#4cc0e8 20%,#3bb24a 40%,#f2c81e 60%,#e0402a 80%,#8a1a6a)}

.view-more{left:517px;top:1944px;width:167px;height:49px;background:var(--purple);font-size:16px}

/* newsletter */
.newsletter-sub{top:2211px;left:0;width:1200px;text-align:center;font-size:14px}
.email-field{left:346px;top:2262px;width:508px;height:48px;border-radius:24px;background:var(--white);overflow:hidden}
.email-field span{position:absolute;left:31px;top:13px;color:#888;font-size:16px}
.email-btn{position:absolute;right:0;top:0;width:131px;height:48px;border-radius:0 24px 24px 0;background:var(--purple);border:1px solid var(--violet);font-size:15px}

/* testimonial */
.avatar{left:560px;top:2565px;width:80px;height:80px;border-radius:50%;background:radial-gradient(circle at 50% 40%,#b58ed6,#6e4aa6)}
.quote{left:230px;top:2656px;width:740px;text-align:center;font-style:italic;font-size:14px;line-height:30px}
.client-name{top:2786px;left:0;width:1200px;text-align:center;font-family:"Cinzel",serif;font-weight:700;color:var(--purple);font-size:16px}
.dots{left:570px;top:2836px;display:flex;gap:4px}
.dots i{width:9px;height:9px;border-radius:50%;background:#2d2a86}
.dots i.on{background:var(--purple)}

/* footer */
.site-footer{left:0;top:2932px;width:1200px;height:395px;background:var(--navy-deep)}
.footer-brand{left:130px;top:3108px;width:175px;text-align:center;font-family:"Cinzel",serif;font-weight:700;font-size:24px}
.social{top:3144px;width:32px;height:32px;border-radius:50%;background:var(--purple)}
.footer-col h4{font-weight:700;font-size:16px;letter-spacing:.3px;margin-bottom:14px}
.footer-col li{list-style:none;font-size:15px;line-height:26px;display:flex;gap:14px}
.footer-col li::before{content:"»";font-weight:700}
.contact li{gap:12px;margin-bottom:12px}
.contact li::before{content:none}
.contact svg{flex:none;margin-top:5px}
.chat{left:967px;top:3189px;width:134px;height:44px;border-radius:22px;background:var(--purple);display:flex;align-items:center;gap:14px;padding-left:9px;font-weight:700;font-size:16px}
.chat i{width:32px;height:32px;border-radius:50%;border:2px solid var(--white);background:#8a5ac0}
.footer-rule{left:45px;top:3256px;width:1110px;height:1px;background:#5d5a94}
.copyright{top:3280px;left:0;width:1200px;text-align:center;font-size:13px}
</style>
</head>
<body>

<header class="abs site-header">
  <nav class="abs main-nav">
    <a style="left:0">HOME</a>
    <a style="left:71px">SOCIAL MEDIA POSTS</a>
    <a style="left:255px">TESTIMONIAL</a>
    <a style="left:384px">CONTACT US</a>
  </nav>
  <svg class="abs nav-search" width="16" height="16" viewBox="0 0 16 16"><circle cx="6.5" cy="6.5" r="5" fill="none" stroke="#fff" stroke-width="2.2"/><line x1="10.2" y1="10.2" x2="14.5" y2="14.5" stroke="#fff" stroke-width="2.5"/></svg>
  <div class="abs lang">ENG ▾</div>
</header>
<div class="abs brand-badge">BRINDMOOR</div>

<section class="abs hero">
  <div class="abs hero-figure" role="img" aria-label="Meditating figure silhouette filled with a starry galaxy above a cloudy sky"></div>
</section>
<h1 class="abs hero-title">BRINDMOOR</h1>
<p class="abs hero-text">Lorem ipsum dolor sit amet, consectetur adipiscing elit, sed do eiusmod tempor incididunt ut labore et dolore magna aliqua. Quis ipsum suspendisse ultrices gravida.</p>
<div class="abs btn hero-btn">GET STARTED</div>

<h2 class="abs section-title" style="top:752px"><b>Our Social</b> Media Feed</h2>
<div class="abs rule" style="top:808px"></div>

<div class="abs filters">
  <span class="filter-active" style="left:304px">All</span>
  <span style="left:368px"><i></i>Meetwall</span>
  <span style="left:513px"><i></i>Chirpnest</span>
  <span style="left:659px"><i></i>Framelane</span>
  <span style="left:803px"><i></i>Boardgrove</span>
</div>

<!-- column 1 -->
<article class="abs post" style="left:111px;top:900px;height:296px">
  <h3>Lorem Ipsum Dolor<i></i></h3><div class="likes">15K LIKES</div>
  <p>Lorem ipsum dolor sit amet, consectetur adipiscing elit, sed do eiusmod tempor incididunt ut labore et dolore.</p>
  <div class="media m-sunset" role="img" aria-label="Person meditating on a rock at sunset with birds"></div>
</article>
<article class="abs post" style="left:111px;top:1221px;height:370px">
  <h3>Lorem Ipsum Dolor<i></i></h3><div class="likes">15K LIKES</div>
  <p>Lorem ipsum dolor sit amet, consectetur adipiscing elit, sed do eiusmod tempor incididunt ut labore et dolore.</p>
  <div class="media m-night" role="img" aria-label="Milky way night sky over a mountain lake"></div>
</article>
<article class="abs post" style="left:111px;top:1612px;height:278px">
  <h3>Lorem Ipsum Dolor<i></i></h3><div class="likes">15K LIKES</div>
  <p>Lorem ipsum dolor sit amet, consectetur adipiscing elit, sed do eiusmod tempor incididunt ut labore et dolore.Lorem ipsum dolor sit amet, consectetur adipiscing elit, sed do eiusmod tempor incididunt ut labore et dolore.Lorem ipsum dolor sit amet, con-</p>
</article>

<!-- column 2 -->
<article class="abs post" style="left:444px;top:900px;height:371px">
  <h3>Lorem Ipsum Dolor<i></i></h3><div class="likes">15K LIKES</div>
  <p>Lorem ipsum dolor sit amet, consectetur adipiscing elit, sed do eiusmod tempor incididunt ut labore et dolore.</p>
  <div class="media m-crowd" role="img" aria-label="Audience attending a workshop presentation"></div>
</article>
<article class="abs post" style="left:444px;top:1314px;height:368px">
  <h3>Lorem Ipsum Dolor<i></i></h3><div class="likes">15K LIKES</div>
  <p>Lorem ipsum dolor sit amet, consectetur adipiscing elit, sed do eiusmod tempor incididunt ut labore et dolore.</p>
  <div class="media m-light" role="img" aria-label="Radiant angelic figure of white light"></div>
</article>
<article class="abs post" style="left:444px;top:1711px;height:179px">
  <h3>Lorem Ipsum Dolor<i></i></h3><div class="likes">15K LIKES</div>
  <p>Lorem ipsum dolor sit amet, consectetur adipiscing elit, sed do eiusmod tempor incididunt ut labore et dolore.</p>
</article>

<!-- column 3 -->
<article class="abs post" style="left:778px;top:900px;height:278px">
  <h3>Lorem Ipsum Dolor<i></i></h3><div class="likes">15K LIKES</div>
  <p>Lorem ipsum dolor sit amet, consectetur adipiscing elit, sed do eiusmod tempor incididunt ut labore et dolore.Lorem ipsum dolor sit amet, consectetur adipiscing elit, sed do eiusmod tempor incididunt ut labore et dolore.Lorem ipsum dolor sit amet, con-</p>
</article>
<article class="abs post" style="left:778px;top:1201px;height:370px">
  <h3>Lorem Ipsum Dolor<i></i></h3><div class="likes">15K LIKES</div>
  <p>Lorem ipsum dolor sit amet, consectetur adipiscing elit, sed do eiusmod tempor incididunt ut labore et dolore.</p>
  <div class="media m-aura" role="img" aria-label="Meditating silhouette with glowing chakras before a rainbow mandala"></div>
</article>
<article class="abs post" style="left:778px;top:1612px;height:278px">
  <h3>Lorem Ipsum Dolor<i></i></h3><div class="likes">15K LIKES</div>
  <p>Lorem ipsum dolor sit amet, consectetur adipiscing elit, sed do eiusmod tempor incididunt ut labore et dolore.Lorem ipsum dolor sit amet, consectetur adipiscing elit, sed do eiusmod tempor incididunt ut labore et dolore.Lorem ipsum dolor sit amet, con-</p>
</article>

<div class="abs btn view-more">VIEW MORE</div>

<h2 class="abs section-title" style="top:2152px;font-size:38px"><b>Subscribe to</b> our Newsletter</h2>
<p class="abs newsletter-sub">Sed ut perspiciatis unde omnis iste natus error sit</p>
<div class="abs email-field"><span>Your email address</span><div class="btn email-btn">SUBSCRIBE</div></div>

<h2 class="abs section-title" style="top:2470px"><b>Our Client</b> Testimonials</h2>
<div class="abs rule" style="top:2525px"></div>
<div class="abs avatar" role="img" aria-label="Client portrait"></div>
<p class="abs quote">Lorem ipsum dolor sit amet, consectetur adipiscing elit, sed do eiusmod tempor incididunt ut labore et dolore magna aliqua. Ut enim ad minim veniam, quis nostrud exercitation ullamco laboris nisi ut aliquip ex ea commodo consequat. Duis aute irure dolor in reprehenderit in voluptate velit esse cillum dolore eu fugiat nulla pariatur. Excepteur sint occaecat cupidatat non proident, sunt in culpa qui officia deserunt mollit anim id est laborum</p>
<div class="abs client-name">MARA ELDWIN</div>
<div class="abs dots"><i></i><i class="on"></i><i></i><i></i><i></i></div>

<footer class="abs site-footer"></footer>
<div class="abs footer-brand">BRINDMOOR</div>
<i class="abs social" style="left:103px"></i>
<i class="abs social" style="left:152px"></i>
<i class="abs social" style="left:201px"></i>
<i class="abs social" style="left:251px"></i>
<i class="abs social" style="left:300px"></i>

<div class="abs footer-col" style="left:402px;top:3002px">
  <h4>QUICK LINKS</h4>
  <ul><li>Home</li><li>social media posts</li><li>testimonials</li><li>Contact Us</li></ul>
</div>
<div class="abs footer-col" style="left:650px;top:3002px">
  <h4>LEGAL</h4>
  <ul><li>Terms of Service</li><li>Privacy Policy</li><li>About Us</li></ul>
</div>
<div class="abs footer-col contact" style="left:905px;top:3002px;width:260px">
  <h4>CONTACT INFO</h4>
  <ul>
    <li><svg width="12" height="15" viewBox="0 0 12 15"><path d="M6 0a6 6 0 0 0-6 6c0 4 6 9 6 9s6-5 6-9a6 6 0 0 0-6-6z" fill="#fff"/><circle cx="6" cy="6" r="2.2" fill="#100d4c"/></svg>Lorem ipsum dolor sit<br>amet, consectetur</li>
    <li><svg width="14" height="14" viewBox="0 0 14 14"><path d="M3 0l3 3-2 2c1 2 3 4 5 5l2-2 3 3-2 3C6 14 0 8 0 3z" fill="#fff"/></svg>1 555 010 2040</li>
    <li><svg width="15" height="12" viewBox="0 0 15 12"><rect width="15" height="12" rx="1.5" fill="#fff"/><path d="M1 1l6.5 5L14 1" fill="none" stroke="#100d4c" stroke-width="1.5"/></svg>info@brindmoormail.com</li>
  </ul>
</div>
<div class="abs chat"><i></i>CHAT</div>
<div class="abs footer-rule"></div>
<p class="abs copyright">© Copyrights 2021 <b>Brindmoor</b> &nbsp; | &nbsp; All Rights Reserved</p>

</body>
</html>
```